A website design for a consultation firm

We are located in Istanbul, Turkey and offers our consultation services to customers interested in investing in Realestate, Education and Investment particularly this coming from Arab world and English speaking countries.

The site should carry our message of deep knowledge about the Turkish markets in the mentioned sectors of interest, sincerity and keenness.

The final deliverable of the winning design should include:
- The source files of the final designs. e.g. AI, PSD ..etc
- The redline markup for the design using a Specctr or any other similar tool.

Target Market(s)

English and Arabic speaking countries with a Turkish theme since we are a Turkish company

Industry/Entity Type

Consulting

Number of Pages Required

2 page

Font styles to use
Sans Serif

Requirements
Must have
• The site should serve the following main sections:
• - Why QVD?
• - Reports & studies
• - Sectors
• - Our team
• - Contact
• We need a design that could be converted into a WordPress theme.
• The design should be in English but should accommodate other languages including RTL.
• You can use the color theme you like as long as it does't dissolve the logo.
• The site should link into our accounts on the following networks:
• - Twitter
• - Facebook
• - LinkedIn
• The design should be responsive and nicely rendered on Desktop, Tablets and Smart phones.
Nice to have
• The site would be nice to balance between being informative and

```html
<!DOCTYPE html>
<html lang="en">
<head>
<meta charset="utf-8">
<title>QVD Consulting</title>
<link href="https://fonts.googleapis.com/css2?family=Ubuntu:wght@400;500;700&family=Open+Sans:ital,wght@0,400;0,600;0,700;1,400&display=swap" rel="stylesheet">
<style>
:root{
  --navy:#1d3b6e;
  --navy-dark:#16305c;
  --red:#c8161d;
  --red-dark:#a80f15;
  --ink:#2b2b2b;
  --muted:#555;
  --grey-bg:#e9e9e9;
  --light:#f4f4f4;
  --footer:#262626;
  --white:#fff;
  --head:'Ubuntu',sans-serif;
  --body:'Open Sans',sans-serif;
}
*{box-sizing:border-box;margin:0;padding:0}
html,body{width:1200px;height:3629px;overflow:hidden}
body{position:relative;font-family:var(--body);color:var(--ink);background:var(--white)}
section,header,footer,div.topbar{position:absolute;left:0;width:1200px}
.topbar{top:0;height:39px;border-bottom:1px solid #eee;font-size:12px;color:#555;display:flex;justify-content:flex-end;align-items:center;gap:44px;padding-right:70px}
.topbar span{display:flex;align-items:center;gap:10px}
.topbar svg{width:16px;height:16px}
.site-header{top:39px;height:99px;border-bottom:1px solid #eee}
.brand{position:absolute;left:48px;top:22px;font-family:var(--head);font-weight:700;font-size:34px;color:var(--red);line-height:1}
.brand small{display:block;font-size:15px;font-weight:700;letter-spacing:1px;margin-top:2px}
.main-nav{position:absolute;right:50px;top:0;height:99px;display:flex;gap:0}
.main-nav a{font-family:var(--head);font-size:15px;font-weight:500;color:var(--ink);text-decoration:none;padding:0 28px;line-height:99px;position:relative}
.main-nav a.active::after{content:"";position:absolute;left:28px;right:28px;bottom:0;height:5px;background:var(--navy)}
.hero{top:138px;height:506px}
.hero-photo{position:absolute;inset:0;background:linear-gradient(90deg,#f3f5f8 0%,#e3e8ee 32%,#9aa5b4 58%,#3f4b5e 80%,#27303f 100%)}
.hero-copy{position:absolute;left:50px;top:102px;width:560px}
.hero h1{font-family:var(--head);font-weight:500;font-size:46px;line-height:1.1;color:var(--navy)}
.hero h1 em{font-style:normal;color:var(--red);display:block}
.hero p{font-size:13.5px;line-height:1.55;margin-top:12px;color:#222}
.btn-outline{display:inline-flex;align-items:center;gap:14px;border:2px solid var(--ink);background:rgba(255,255,255,.85);padding:12px 22px;font-size:16px;color:var(--ink);margin-top:42px;border-radius:3px}
.why{top:644px;height:430px}
.why-panel{position:absolute;left:0;top:0;width:435px;height:430px;background:var(--navy);color:var(--white);padding:32px 62px}
.why-panel h2{font-family:var(--head);font-weight:500;font-size:33px;letter-spacing:1px;border-bottom:1px solid rgba(255,255,255,.3);padding-bottom:14px}
.why-panel p{font-size:13.5px;line-height:1.55;margin-top:16px}
.why-panel .btn-light{display:inline-flex;align-items:center;gap:16px;border:2px solid var(--white);padding:12px 22px;font-size:16px;margin-top:30px}
.services{position:absolute;left:435px;top:0;width:765px;height:430px;background:var(--grey-bg)}
.service{position:absolute;width:330px;display:flex;gap:18px}
.service .ico{width:52px;height:52px;flex:none;border-radius:50%;background:var(--navy);display:flex;align-items:center;justify-content:center}
.service .ico.ring{background:transparent;border:3px solid var(--navy)}
.service h3{font-family:var(--head);font-weight:500;font-size:17px;color:var(--navy)}
.service p{font-size:12.5px;line-height:1.6;color:var(--muted);margin-top:6px}
.section-title{font-family:var(--head);font-weight:500;font-size:33px;text-align:center;letter-spacing:1px;color:var(--ink)}
.sectors{top:1074px;height:570px;border-bottom:1px solid #ddd}
.sectors .section-title{position:absolute;top:52px;width:100%}
.sector-card{position:absolute;top:128px;width:342px}
.sector-card .photo{height:191px;background:linear-gradient(180deg,#e9ecef,#c9ced4)}
.sector-card h3{font-family:var(--head);font-weight:500;font-size:23px;margin-top:18px}
.sector-card p{font-size:13px;line-height:1.55;color:var(--muted);margin-top:6px;text-align:justify}
.btn-red{display:inline-block;border:2px solid var(--red);padding:6px 12px;font-size:14px;margin-top:16px;color:var(--ink)}
.testimonials{top:1645px;height:545px;text-align:center}
.testimonials .section-title{margin-top:38px}
.quote-mark{width:48px;height:48px;border-radius:50%;border:2px solid #e8541e;margin:60px auto 0;color:#e8541e;font-family:var(--head);font-weight:700;font-size:26px;line-height:44px}
.testimonials blockquote{width:880px;margin:28px auto 0;font-style:italic;font-size:13.5px;line-height:2.1;color:#6b8a8c}
.testimonials .by{font-size:11px;color:#888;margin-top:22px}
.testimonials .author{font-family:var(--head);font-weight:700;font-size:13px;color:var(--navy);margin-top:6px}
.hex-group{width:180px;height:118px;margin:14px auto 0}
.cta-bar{top:2192px;left:48px!important;width:1104px!important;height:94px;background:var(--red);color:var(--white);display:flex;border-radius:3px}
.cta-bar .half{flex:1;display:flex;align-items:center;padding-left:20px;gap:18px}
.cta-bar .half + .half{border-left:2px solid rgba(255,255,255,.5);padding-left:38px}
.cta-bar .lbl{font-family:var(--head);font-size:16px;line-height:1.5}
.cta-bar .val{font-family:var(--head);font-size:24px;margin-left:14px}
.cta-or{position:absolute;left:536px;top:30px;width:34px;height:34px;border-radius:50%;background:var(--navy);color:#fff;font-size:12px;font-weight:700;text-align:center;line-height:34px}
.team{top:2288px;height:489px;background:var(--grey-bg)}
.team .section-title{margin-top:38px}
.member{position:absolute;top:131px;width:240px;text-align:center}
.member .avatar{width:174px;height:174px;border-radius:50%;margin:0 auto;background:linear-gradient(180deg,#dfe6ec,#9fb0c0);border:4px solid #fff}
.member h3{font-family:var(--head);font-weight:500;font-size:17px;margin-top:22px}
.member p{font-size:13px;line-height:1.6;color:var(--muted);margin-top:8px}
.member .social{display:flex;justify-content:center;gap:10px;margin-top:12px}
.member .social i{width:28px;height:28px;border:2px solid var(--ink);border-radius:50%;display:block}
.consult{top:2777px;height:452px}
.consult-photo{position:absolute;inset:0;background:linear-gradient(180deg,#c9d3dc 0%,#dfe3e6 45%,#8f97a0 100%)}
.consult h2{position:absolute;left:48px;top:80px;font-family:var(--head);font-weight:700;font-size:35px;color:var(--red)}
.consult p{position:absolute;left:48px;top:136px;font-family:var(--head);font-weight:500;font-size:17px;color:#111}
.consult .btn-outline{position:absolute;left:54px;top:197px;margin:0;border-color:#fff;background:transparent;color:#111;padding:12px 22px}
.footer{top:3229px;height:400px;background:var(--footer);color:#fff;text-align:center}
.newsletter{top:3096px;left:48px!important;width:1104px!important;height:211px;background:var(--navy);color:#fff;text-align:center;z-index:2}
.newsletter h2{font-family:var(--head);font-weight:700;font-size:33px;margin-top:24px;letter-spacing:1px}
.newsletter p{font-family:var(--head);font-weight:500;font-size:17px;margin-top:0}
.sub-form{display:flex;justify-content:center;margin-top:30px}
.sub-form span{width:470px;height:52px;background:#fff;color:#888;text-align:left;padding:14px 18px;font-size:15px}
.sub-form b{height:52px;background:var(--navy-dark);font-family:var(--head);font-weight:500;font-size:17px;padding:14px 24px;border:1px solid rgba(255,255,255,.2)}
.footer .brand-foot{font-family:var(--head);font-weight:700;font-size:34px;color:#bbb;margin-top:126px;line-height:1}
.footer .brand-foot small{display:block;font-size:14px}
.footer nav{font-family:var(--head);font-size:16px;margin-top:40px;letter-spacing:.5px}
.footer .copy{font-family:var(--head);font-size:15px;margin-top:6px}
.footer .diamonds{display:flex;justify-content:center;gap:16px;margin-top:40px}
.footer .diamonds i{width:34px;height:34px;background:#fff;transform:rotate(45deg);display:block}
</style>
</head>
<body>

<div class="topbar">
  <span><svg viewBox="0 0 16 16"><path d="M4 1l3 3-2 2c1 2 3 4 5 5l2-2 3 3-2 2C7 14 2 9 2 3z" fill="none" stroke="#2aa6d6" stroke-width="1.3"/></svg>Call free: 212 555 0147</span>
  <span><svg viewBox="0 0 16 16"><rect x="1" y="3" width="14" height="10" fill="none" stroke="#2aa6d6" stroke-width="1.3"/><path d="M1 3l7 6 7-6" fill="none" stroke="#2aa6d6" stroke-width="1.3"/></svg>hello@qvdadvisory.com</span>
  <span><svg viewBox="0 0 16 16"><path d="M8 15s5-5 5-9A5 5 0 0 0 3 6c0 4 5 9 5 9z" fill="none" stroke="#2aa6d6" stroke-width="1.3"/><circle cx="8" cy="6" r="1.8" fill="#2aa6d6"/></svg>24 Harbor Lane, Istanbul 34000 TR</span>
  <span>English ▾</span>
</div>

<header class="site-header">
  <div class="brand">QVD<small>consulting</small></div>
  <nav class="main-nav">
    <a class="active">WHY QVD?</a><a>REPORTS &amp; STUDIES</a><a>SECTORS</a><a>OUR TEAM</a><a>CONTACT</a>
  </nav>
</header>

<section class="hero">
  <div class="hero-photo" role="img" aria-label="Two consultants in suits reviewing work together at a laptop"></div>
  <div class="hero-copy">
    <h1>Helping your business<em>build and grow</em></h1>
    <p>Lorem Ipsum is simply dummy text of the printing and typesetting industry. Lorem Ipsum has been the industry's standard dummy text ever since the 1500s,</p>
    <span class="btn-outline">Start Your Project <b>›</b></span>
  </div>
</section>

<section class="why">
  <div class="why-panel">
    <h2>WHY QVD?</h2>
    <p>Lorem Ipsum is simply dummy text of the printing and typesetting industry. Lorem Ipsum has been the industry's standard dummy text ever since the 1500s, when an unknown printer took a galley text of the printing and typesetting industry. Lorem Ipsum has been the industry's standard dummy text ever since the 1500s, when an unknown printer took a galley...</p>
    <span class="btn-light">Read More <b>›</b></span>
  </div>
  <div class="services">
    <div class="service" style="left:26px;top:26px"><div class="ico ring"><svg width="28" height="28" viewBox="0 0 28 28"><circle cx="14" cy="14" r="10" fill="none" stroke="#1d3b6e" stroke-width="2"/><path d="M4 14h20M14 4v20" stroke="#1d3b6e" stroke-width="1.5"/></svg></div><div><h3>Technology</h3><p>Company that offers design and build services for you from initial sketches to the final production.</p></div></div>
    <div class="service" style="left:420px;top:26px"><div class="ico"><svg width="26" height="26" viewBox="0 0 26 26"><rect x="6" y="8" width="14" height="11" fill="none" stroke="#fff" stroke-width="2"/><path d="M10 8V5h6v3" fill="none" stroke="#fff" stroke-width="2"/></svg></div><div><h3>Business</h3><p>Company that offers design and build services for you from initial sketches to the final production.</p></div></div>
    <div class="service" style="left:26px;top:171px"><div class="ico"><svg width="26" height="26" viewBox="0 0 26 26"><path d="M5 20l6-6 4 4 6-9" fill="none" stroke="#fff" stroke-width="2"/></svg></div><div><h3>Enterprise Integration</h3><p>Company that offers design and build services for you from initial sketches to the final production.</p></div></div>
    <div class="service" style="left:420px;top:171px"><div class="ico"><svg width="26" height="26" viewBox="0 0 26 26"><rect x="4" y="6" width="18" height="12" fill="none" stroke="#fff" stroke-width="2"/><path d="M9 22h8" stroke="#fff" stroke-width="2"/></svg></div><div><h3>IT Consulting</h3><p>Company that offers design and build services for you from initial sketches to the final production.</p></div></div>
    <div class="service" style="left:26px;top:316px"><div class="ico ring"><svg width="26" height="26" viewBox="0 0 26 26"><rect x="8" y="4" width="10" height="18" rx="2" fill="none" stroke="#1d3b6e" stroke-width="2"/></svg></div><div><h3>Application Developement</h3><p>Company that offers design and build services for you from initial sketches to the final production.</p></div></div>
    <div class="service" style="left:420px;top:316px"><div class="ico"><svg width="26" height="26" viewBox="0 0 26 26"><circle cx="13" cy="9" r="4" fill="none" stroke="#fff" stroke-width="2"/><path d="M5 22c1-5 15-5 16 0" fill="none" stroke="#fff" stroke-width="2"/></svg></div><div><h3>Staff Augmentation</h3><p>Company that offers design and build services for you from initial sketches to the final production.</p></div></div>
  </div>
</section>

<section class="sectors">
  <h2 class="section-title">SECTORS</h2>
  <article class="sector-card" style="left:48px"><div class="photo" role="img" aria-label="Consultant on a phone call at a desk with a laptop"></div><h3>Dashbords</h3><p>Our Offshore Development Center at Hyderabad, India is comprised of an excellent delivery facility and staff dedicated to our customer's IT requirements. The center consists of a team...</p><span class="btn-red">Read More</span></article>
  <article class="sector-card" style="left:429px"><div class="photo" role="img" aria-label="Man reviewing documents at an office desk"></div><h3>Data Warehousing</h3><p>Our Offshore Development Center at Hyderabad, India is comprised of an excellent delivery facility and staff dedicated to our customer's IT requirements. The center consists of a team...</p><span class="btn-red">Read More</span></article>
  <article class="sector-card" style="left:812px"><div class="photo" role="img" aria-label="Woman working at a laptop in a bright office"></div><h3>BPM</h3><p>Our Offshore Development Center at Hyderabad, India is comprised of an excellent delivery facility and staff dedicated to our customer's IT requirements. The center consists of a team...</p><span class="btn-red">Read More</span></article>
</section>

<section class="testimonials">
  <h2 class="section-title">Tesimonials</h2>
  <div class="quote-mark">“</div>
  <blockquote>Lorem Ipsum is simply dummy text of the printing and typesetting industry. Lorem Ipsum has been the industry's standard dummy text ever since the 1500s, when an unknown printer took a galley of type and scrambled it to make a type specimen book. It has survived not only five centuries, but also the leap into electronic typesetting, remaining essentially unchanged.</blockquote>
  <div class="by">by</div>
  <div class="author">DR. SELIM</div>
  <svg class="hex-group" viewBox="0 0 180 118" role="img" aria-label="Hexagon portraits of clients">
    <polygon points="45,2 70,16 70,44 45,58 20,44 20,16" fill="#b9a79a"/>
    <polygon points="90,2 115,16 115,44 90,58 65,44 65,16" fill="#e8683a"/>
    <polygon points="135,2 160,16 160,44 135,58 110,44 110,16" fill="#9c9590"/>
    <polygon points="67,58 92,72 92,100 67,114 42,100 42,72" fill="#a79b92"/>
    <polygon points="113,58 138,72 138,100 113,114 88,100 88,72" fill="#b7aca3"/>
  </svg>
</section>

<section class="cta-bar">
  <div class="half"><svg width="50" height="50" viewBox="0 0 50 50"><circle cx="20" cy="16" r="9" fill="#fff"/><path d="M4 46c2-14 30-14 32 0z" fill="#fff"/></svg><span class="lbl">Call now<br>for free consultation</span><span class="val">: +90 (212) 555 0190</span></div>
  <div class="half"><svg width="46" height="46" viewBox="0 0 46 46"><circle cx="23" cy="23" r="21" fill="none" stroke="#fff" stroke-width="2"/><rect x="12" y="15" width="22" height="16" fill="none" stroke="#fff" stroke-width="2"/><path d="M12 15l11 9 11-9" fill="none" stroke="#fff" stroke-width="2"/></svg><span class="lbl">Mail now<br>free consultation</span><span class="val">: info@qvdadvisory</span></div>
  <div class="cta-or">OR</div>
</section>

<section class="team">
  <h2 class="section-title">OUR TEAM</h2>
  <div class="member" style="left:66px"><div class="avatar" role="img" aria-label="Team member portrait"></div><h3>AREN TOLVAR</h3><p>Sic tempus fugit esperanto hiccup<br>estrogen. Glorious baklava.</p><div class="social"><i></i><i></i><i></i><i></i></div></div>
  <div class="member" style="left:344px"><div class="avatar" role="img" aria-label="Team member portrait"></div><h3>AREN TOLVAR</h3><p>Sic tempus fugit esperanto hiccup<br>estrogen. Glorious baklava.</p><div class="social"><i></i><i></i><i></i><i></i></div></div>
  <div class="member" style="left:621px"><div class="avatar" role="img" aria-label="Team member portrait"></div><h3>AREN TOLVAR</h3><p>Sic tempus fugit esperanto hiccup<br>estrogen. Glorious baklava.</p><div class="social"><i></i><i></i><i></i><i></i></div></div>
  <div class="member" style="left:895px"><div class="avatar" role="img" aria-label="Team member portrait"></div><h3>AREN TOLVAR</h3><p>Sic tempus fugit esperanto hiccup<br>estrogen. Glorious baklava.</p><div class="social"><i></i><i></i><i></i><i></i></div></div>
</section>

<section class="consult">
  <div class="consult-photo" role="img" aria-label="Person in a hooded top working on a laptop on a wooden deck under a cloudy sky"></div>
  <h2>CONSULTING SERVICE</h2>
  <p>We are providing wide range of Consulting Services &amp; World wide happy Clients</p>
  <span class="btn-outline">Start Your Project <b>›</b></span>
</section>

<footer class="footer">
  <div class="brand-foot">QVD<small>consulting</small></div>
  <nav>HOME • SOLUTIONS • SERVICES • COMPANY • CONTACT</nav>
  <div class="copy">Copyright © 2007 - 2016 QVD Consulting, Inc. All Rights Reserved</div>
  <div class="diamonds"><i></i><i></i><i></i><i></i></div>
</footer>

<section class="newsletter">
  <h2>NEWS LETTER</h2>
  <p>Enter your email adrress for getting updates</p>
  <div class="sub-form"><span>Enter your Email</span><b>Subscribe</b></div>
</section>

</body>
</html>
```